Building Company Business Card Design

I am looking to get a business card designed for my Building Company. Please find the logo attached.

Industry/Entity Type

Business

Contact Information for Business Card

Mobile 0472 913 706
Email admin@harbourlineconstruct.com.au
Website www.harbourlineconstruct.com.au

Colors
0255a3

```html
<!DOCTYPE html>
<html lang="en">
<head>
<meta charset="utf-8">
<title>Harbourline Construct – Business Card</title>
<link rel="stylesheet" href="https://fonts.googleapis.com/css2?family=Roboto:wght@400;500;700&family=Roboto+Condensed:wght@700&display=swap">
<style>
  :root {
    --brand-blue: #0255a3;
    --stage: #2b2b2b;
    --card-dark: #1c1f22;
    --card-dark-edge: #15171a;
    --card-light: #f1f1f1;
    --text-grey: #4a4a4a;
    --muted-grey: #6f7378;
  }
  * { margin: 0; padding: 0; box-sizing: border-box; }
  html, body { width: 1200px; height: 960px; overflow: hidden; }
  body {
    position: relative;
    background: var(--stage);
    font-family: "Roboto", Arial, sans-serif;
  }
  .card { position: absolute; border-radius: 18px; }

  .card-stack {
    left: 316px; top: 104px; width: 600px; height: 360px;
    background: var(--card-dark-edge);
  }
  .card-back {
    left: 322px; top: 97px; width: 596px; height: 356px;
    background: var(--card-dark);
  }
  .card-back .brand {
    position: absolute; right: 46px; top: 268px;
    display: flex; align-items: center; gap: 10px;
  }
  .card-back .web {
    position: absolute; right: 48px; top: 306px;
    font-size: 14px; letter-spacing: 1.6px; color: var(--muted-grey);
  }

  .brand-mark { width: 12px; height: 12px; background: var(--brand-blue); }
  .brand-name {
    font-family: "Roboto", Arial, sans-serif;
    font-weight: 700; color: var(--brand-blue);
    text-transform: uppercase; line-height: 1.05;
  }
  .card-back .brand-name { font-size: 24px; letter-spacing: 1px; }

  .card-front {
    left: 320px; top: 493px; width: 600px; height: 342px;
    background: var(--card-light);
    overflow: hidden;
  }
  .card-front .brand {
    position: absolute; left: 46px; top: 150px;
    display: flex; align-items: center; gap: 8px;
  }
  .card-front .brand-name { font-size: 19px; letter-spacing: 0.5px; }

  .holder { position: absolute; left: 309px; top: 66px; }
  .holder-name {
    font-family: "Roboto Condensed", "Arial Narrow", sans-serif;
    font-weight: 700; font-size: 24px; color: var(--brand-blue);
    letter-spacing: 0.3px; line-height: 1;
  }
  .holder-title {
    font-size: 14.5px; font-weight: 500; color: var(--text-grey);
    margin-top: 6px; letter-spacing: 0.3px;
  }
  .rule {
    position: absolute; left: 309px; right: 0; top: 115px;
    height: 2px; background: var(--brand-blue);
  }
  .address {
    position: absolute; left: 309px; top: 146px;
    font-size: 14px; line-height: 18px; color: var(--text-grey);
    font-style: normal;
  }
  .contacts {
    position: absolute; left: 309px; top: 217px;
    list-style: none; font-size: 14px; color: var(--text-grey);
  }
  .contacts li { display: flex; align-items: center; height: 19.5px; gap: 8px; }
  .contacts svg { width: 13px; height: 13px; fill: var(--brand-blue); flex: none; }
</style>
</head>
<body>
  <div class="card card-stack" aria-hidden="true"></div>
  <section class="card card-back" aria-label="Card back">
    <div class="brand">
      <span class="brand-mark"></span>
      <span class="brand-name">Harbourline Construct</span>
    </div>
    <p class="web">www.harbourlineconstruct.com.au</p>
  </section>

  <section class="card card-front" aria-label="Card front">
    <div class="brand">
      <span class="brand-mark"></span>
      <span class="brand-name">Harbourline<br>Construct</span>
    </div>

    <div class="holder">
      <h1 class="holder-name">DANIEL REYES</h1>
      <p class="holder-title">CEO/FOUNDER</p>
    </div>
    <div class="rule"></div>

    <address class="address">412 Wattle Street<br>Ultimo, NSW 2007</address>

    <ul class="contacts">
      <li>
        <svg viewBox="0 0 24 24"><path d="M6.6 10.8a15.2 15.2 0 0 0 6.6 6.6l2.2-2.2a1 1 0 0 1 1-.25 11.4 11.4 0 0 0 3.6.57 1 1 0 0 1 1 1V20a1 1 0 0 1-1 1A17 17 0 0 1 3 4a1 1 0 0 1 1-1h3.5a1 1 0 0 1 1 1c0 1.25.2 2.45.57 3.57a1 1 0 0 1-.25 1z"/></svg>
        0472 913 706
      </li>
      <li>
        <svg viewBox="0 0 24 24"><path d="M2 5h20v14H2z" fill="none"/><path d="M2 5h20v2l-10 6L2 7zM2 9l10 6 10-6v10H2z"/></svg>
        admin@harbourlineconstruct.com.au
      </li>
      <li>
        <svg viewBox="0 0 24 24"><circle cx="12" cy="12" r="10"/><path d="M2 12h20M12 2c3 3 3 17 0 20M12 2c-3 3-3 17 0 20" stroke="#f1f1f1" stroke-width="1.6" fill="none"/></svg>
        www.harbourlineconstruct.com.au
      </li>
    </ul>
  </section>
</body>
</html>
```